Sehr angenehme und professionelle Zusammenarbeit!
Zielgruppe
Ich bin ein Consultant, der sich jetzt selbständig macht. Alles weitere steht in meinen Briefing. Dort findet ihr Fotos, mein Logo und damit auch die Farben, die ich mir wünsche. Meine Zielgruppe sind überwiegend Firmen, aber auch deren Mitarbeitende.
Aufgabenstellung
Die Struktur habe ich versucht zu beschreiben und hoffentlich auch alles über mich und mein Business. Ich freue mich auf eure kreativen und individuellen Vorschläge und bemühe mich zeitnah Feedback zu geben. Manchmal kann es den einen oder anderen Tag dauern. Bei Fragen gerne melden. Ich werde die Fragen, die für alle relevant sind auch im allgemeinen Kommentarfeld veröffentlichen.

```html
<!DOCTYPE html>
<html lang="de">
<head>
<meta charset="utf-8">
<title>Jonas Brenner – Beratung für komplexe Personalsituationen</title>
<link href="https://fonts.googleapis.com/css2?family=Montserrat:wght@400;500;600;700&display=swap" rel="stylesheet">
<style>
:root{
  --navy:#1d2a6b;
  --brand:#0d3e8f;
  --text:#3a3f55;
  --muted:#6a7088;
  --line:#1d2a6b;
  --stage:#4a7fd1;
  --sky:#dce6f5;
  --white:#ffffff;
  --card-line:#c8cdd8;
}
*{box-sizing:border-box;margin:0;padding:0}
html,body{width:1200px;height:4800px;overflow:hidden}
body{background:var(--stage);font-family:"Montserrat",sans-serif;color:var(--text);position:relative}
.page{position:absolute;left:0;top:0;width:1200px;height:4512px;background:var(--white)}
.abs{position:absolute}
/* hero */
.hero{left:0;top:0;width:1200px;height:707px;border-bottom:3px solid var(--navy)}
.hero-photo{left:418px;top:0;width:782px;height:704px;background:linear-gradient(90deg,#f3f6fb 0%,#e4ecf7 45%,#d6e2f3 100%)}
.brand-dot{left:199px;top:100px;width:20px;height:20px;border-radius:50%;background:var(--navy)}
.brand{left:0;width:418px;text-align:center;top:138px;font-weight:600;font-size:20px;letter-spacing:4px;color:var(--navy);text-transform:uppercase}
.brand-tag{left:0;width:418px;text-align:center;top:168px;font-weight:500;font-size:10px;letter-spacing:2px;color:var(--navy);text-transform:uppercase}
.nav{left:0;width:418px;top:250px;text-align:center;list-style:none}
.nav li{height:53px;font-size:12px;color:var(--muted)}
.nav li span{display:inline-block;padding:9px 0}
.nav li.active span{border:2px solid var(--navy);padding:7px 12px;font-weight:700;color:var(--navy)}
/* section headings */
.mark{width:14px;height:14px;border-radius:50%;background:var(--navy);left:593px}
.heading{left:0;width:1200px;text-align:center;font-weight:600;font-size:16px;color:var(--navy)}
.rule{display:inline-block;width:90px;height:1px;background:var(--line);vertical-align:middle;margin:0 14px}
.sub{left:0;width:1200px;text-align:center;font-weight:700;font-size:17px;color:var(--navy)}
.copy{left:280px;width:640px;font-size:11.5px;line-height:17px;color:var(--text)}
.copy p{margin-bottom:12px}
.btn{display:inline-block;background:var(--brand);color:var(--white);font-size:11px;padding:6px 14px}
.btn::after{content:" ›";font-weight:700}
/* cards */
.card{border:2px solid var(--navy);padding:24px 22px;background:var(--white)}
.card h3{font-size:13px;font-weight:700;color:var(--navy);margin-bottom:16px}
.card p{font-size:10.5px;line-height:16px;color:var(--text)}
.offer{border:1px solid var(--card-line);box-shadow:0 3px 8px rgba(0,0,0,.15);padding:34px 22px;background:var(--white)}
.offer h3{text-align:center;font-size:11.5px;font-weight:700;color:var(--navy);line-height:20px;margin-bottom:28px;white-space:nowrap}
.offer p{font-size:10.5px;line-height:16px;margin-bottom:22px}
/* about */
.portrait{left:280px;top:3294px;width:192px;height:420px;background:linear-gradient(180deg,#e9edf3,#c9d4e4)}
.about{left:499px;top:3294px;width:421px}
.about h4{font-size:12px;font-weight:700;color:var(--navy);margin-bottom:10px}
.about p{font-size:10.5px;line-height:16px;margin-bottom:20px}
.blog{border:1px solid var(--card-line);border-top:2px solid var(--navy);padding:30px 20px;background:var(--white)}
.blog h3{font-size:11.5px;font-weight:700;color:var(--navy);margin-bottom:16px}
.blog p{font-size:10.5px;line-height:16px;margin-bottom:16px}
/* footer */
.footer{left:0;top:4188px;width:1200px;height:324px;background:var(--sky);border-top:3px solid var(--navy)}
.foot-dot{left:280px;top:4360px;width:20px;height:20px;border-radius:50%;background:var(--navy)}
.foot-brand{left:130px;top:4400px;width:320px;text-align:center;color:var(--navy)}
.foot-brand .name{font-size:15px;font-weight:700}
.foot-brand .tag{font-size:13px;font-weight:600;margin-top:8px}
.foot-brand .tag .rule{width:60px;margin:0 10px}
.foot-brand .claim{font-size:12px;font-weight:600;margin-top:8px}
.foot-nav{list-style:none;font-size:11px;color:var(--muted);text-align:center}
.foot-nav li{height:52px}
.foot-nav li.active span{border:2px solid var(--navy);padding:6px 12px;font-weight:700;color:var(--navy)}
</style>
</head>
<body>
<main class="page">
  <header class="abs hero">
    <div class="abs hero-photo" role="img" aria-label="Porträtfoto des Beraters, sitzend in grauem Pullover vor hellblauem Hintergrund"></div>
    <div class="abs brand-dot"></div>
    <div class="abs brand">Jonas Brenner</div>
    <div class="abs brand-tag">Klar. Fair. Nachhaltig.</div>
    <ul class="abs nav">
      <li class="active"><span>Home</span></li>
      <li><span>Prozessberatung</span></li>
      <li><span>Situationsanalyse</span></li>
      <li><span>Energie-Coaching</span></li>
      <li><span>Speeches &amp; Vorträge</span></li>
      <li><span>Über Mich</span></li>
      <li><span>Kontakt</span></li>
    </ul>
  </header>

  <div class="abs mark" style="top:800px"></div>
  <h2 class="abs heading" style="top:830px"><span class="rule"></span>Klar. Fair. Nachhaltig.<span class="rule"></span></h2>
  <div class="abs sub" style="top:858px">Beratung für komplexe Personalsituationen</div>
  <div class="abs copy" style="top:906px">
    <p>Personalprobleme sind eine normale Begleiterscheinung in unserem Zeit voll Wandel. Im Daily Business werden diese Situationen jedoch selten tiefer analysiert und häufig nur kosmetisch behandelt. Ein Aussitzen hier, eine Mediation dort, ein plötzliches Abfindungsangebot da. Vielleicht auch schon zahlreiche Gespräche oder Coachings, die nicht zur gewünschten Veränderung führten.</p>
    <p>Die Folge: die Motivation sinkt. Nicht nur bei dem/der jeweiligen Mitarbeitenden, auch im Teamumfeld und bei der Führungskraft. Frustration steigt, es kommt zu Fehlzeiten, die Produktivität lässt nach, mitunter können Ziele nicht erreicht werden. Die Gerüchteküche kocht vor sich hin.</p>
    <p>Meine Beratung und Prozessbegleitung schließt hier eine Lücke. Sie bietet nachhaltige Lösungen bei komplexen und dysfunktionalen Personalsituationen an, die alle Seiten einbeziehen: Mitarbeitende/r, Führungskraft, Organisation.</p>
  </div>

  <div class="abs mark" style="top:1140px"></div>
  <h2 class="abs heading" style="top:1177px"><span class="rule"></span>Ihr Nutzen:<span class="rule"></span></h2>
  <div class="abs sub" style="top:1205px">Von Lose zu Win für alle Seiten</div>
  <div class="abs copy" style="top:1250px">
    <p>Während auf individueller Ebene Menschen ihr Potenzial nicht entfalten können und oft lange an der Situation leiden, entstehen auf organisationaler Ebene wirtschaftliche Einbußen und Imageschäden. Selten ist nur eine Person betroffen, auch wenn es sich oft auf eine Person fokussiert. Die Ursachen sind multifaktoriell und langwierig, die negative Wirkung strahlt auf den/die Mitarbeitende/n, die Führungskraft, das Team und die Organisation aus.</p>
    <p>Klar. Fair. Nachhaltig. Bedeutet nicht, dass alle Beteiligten ihre optimale Wunschvorstellung erfüllen. Es bedeutet, dass wir die bestmögliche Lösung erarbeiten, in die alle Sichtweisen einfließen. Wahlmöglichkeiten bestehen und eine dysfunktionale Situation nachhaltig aufgelöst wird. Und letztendlich sogar Entwicklung entsteht. „Boost or Leave" – es gibt immer diese beiden Möglichkeiten: Entweder eine echte Entwicklung, an der alle beteiligt sind, oder ein Verlassen der Situation, das gemeinsam entschieden wird.</p>
    <span class="btn">Zum Kennenlerngespräch</span>
  </div>

  <div class="abs card" style="left:176px;top:1562px;width:400px;height:282px">
    <h3>Führungskraft</h3>
    <p>Wiederkehrende Konfliktsituationen mit einer/m Mitarbeitenden. Disharmonie im Team, nicht genutzte Potenziale, mitunter steigende Fehlzeiten und Schwierigkeiten, die vorgegebenen Ziele zu erreichen. Gesprächs- und Lösungsversuche kosten Zeit und Energie. Durch und Beratung analysieren wir die Situation, schauen auf Ihren Anteil und finden Lösungsansätze, die die Funktionalität des Teams wiederherstellen, die/den betroffenen Mitarbeitende/n einbeziehen und Ihr Handlungsspektrum erweitern.</p>
  </div>
  <div class="abs card" style="left:623px;top:1513px;width:402px;height:337px">
    <h3>Mitarbeitende/r</h3>
    <p>Oft beginnt es mit Unzufriedenheit, vielleicht fehlender Wertschätzung oder Überlastung und einem angeknacksten Vertrauen in sich selbst, in die Führungskraft oder Organisation. In einer andauernden Konfliktsituation kommen später physische und psychische Belastungssymptome, mitunter Fehlzeiten hinzu. In den Beratungsterminen berücksichtigen wir gemeinsam Ihre Persönlichkeitsmerkmale, Erfolgs- und Misserfolgsgeschichten, das Unternehmensumfeld und Ihre persönlichen Umstände. Um zu verstehen, wie die Situation entstehen konnte und um neue Lösungswege auszumachen. Oft lässt sich herausfinden, wo der Platz ist, an dem Sie bestmöglich wirken können. Manchmal ist es ein mutiges Vorwärts zu etwas Neuem. Aber es bleibt Ihre Wahl.</p>
  </div>
  <div class="abs mark" style="top:1858px"></div>
  <div class="abs card" style="left:402px;top:1897px;width:400px;height:321px">
    <h3>Organisation</h3>
    <p>Eine Konfliktsituation bleibt nie auf eine Person beschränkt. Neben wirtschaftlichen Einbußen für die Organisation, verursacht durch Fehlzeiten, Ausfälle und Nichterreichung von Zielen, gibt es fast immer einen Imageschaden. Spannungen breiten sich über das Team hinaus aus, Gerüchte brodeln, Ungerechtigkeitsdiskussionen finden statt, das Vertrauen in die Führung sinkt, Verunsicherung ist spürbar. In meinem Beratungsprozess kläre ich, welche internen Lösungen machbar sind, und bespreche transparente Kommunikationsmöglichkeiten. So können komplexe Personalsituationen dazu beitragen, Ihr Unternehmen als lernende Organisation zu entwickeln. Eine schwierige Situation kann zu einer Entwicklungschance werden.</p>
  </div>

  <div class="abs mark" style="top:2298px"></div>
  <h2 class="abs heading" style="top:2337px"><span class="rule"></span>Meine Angebote:<span class="rule"></span></h2>
  <div class="abs sub" style="top:2363px">Von der Analyse über Beratung bis zur Wissensvermittlung</div>

  <div class="abs offer" style="left:280px;top:2428px;width:286px;height:318px">
    <h3>Prozessberatung und -begleitung:<br>Ganzheitlich vom Problem zur Lösung</h3>
    <p>Mit meinem 7-Phasen-Modell berate und begleite ich Mitarbeitende und Führungskraft individuell und gemeinsam bei der Lösungsfindung und -entscheidung. Gemeinsames Commitment vorausgesetzt, immer abgestimmt auf die Rahmenbedingungen der Organisation.</p>
    <span class="btn">Prozessberatung</span>
  </div>
  <div class="abs offer" style="left:619px;top:2428px;width:303px;height:318px">
    <h3>Situationsanalyse:<br>Ein Anfang, mehr Klarheit</h3>
    <p>Im Einzel-Coaching für Führungskräfte und Mitarbeitende analysiere ich mit Ihnen Ihren konkreten Fall. Wir beleuchten Ursachen und eruieren Lösungsoptionen. Damit Sie mehr Klarheit gewinnen und Ihre Handlungsmöglichkeiten erweitern können.</p>
    <span class="btn">Situationsanalyse</span>
  </div>
  <div class="abs offer" style="left:280px;top:2765px;width:286px;height:315px">
    <h3>Persönliches Energie-Coaching:<br>Mit Kraft neue Wege gehen</h3>
    <p>Im 1:1 begleite und berate ich Sie ganzheitlich über mehrere Monate. Individuell, persönlich und intensiv. Damit Sie wieder in Ihre Kraft kommen und Ihren Weg raus aus einer dysfunktionalen beruflichen Situation finden. Sie stehen im Mittelpunkt – mit Körper, Geist und Seele.</p>
    <span class="btn">Energie-Coaching</span>
  </div>
  <div class="abs offer" style="left:619px;top:2765px;width:303px;height:315px">
    <h3>Keynote Speeches &amp; Vorträge:<br>Impulse für neue Denkweisen</h3>
    <p>Denken Sie Personalprobleme neu und erkennen Sie die Entwicklungschancen. Welche Faktoren spielen eine Rolle? Wie wirken sie sich aus? Wie lassen sich nachhaltige Lösungen finden? In meinen Vorträgen gebe ich Impulse und teile mein Erfahrungswissen zu Lösungsstrategien, die alle Beteiligten einbeziehen.</p>
    <span class="btn">Speeches &amp; Vorträge</span>
  </div>

  <div class="abs mark" style="top:3166px"></div>
  <h2 class="abs heading" style="top:3205px">Ich bin Jonas Brenner und mein Anspruch ist:</h2>
  <div class="abs sub" style="top:3233px"><span class="rule"></span>Klar. Fair. Nachhaltig.<span class="rule"></span></div>
  <div class="abs portrait" role="img" aria-label="Porträtfoto des Beraters im hellblauen Hemd"></div>
  <div class="abs about">
    <h4>Meine Motivation</h4>
    <p>Ich möchte Menschen unterstützen, sich aus dysfunktionalen Arbeitssituationen zu lösen, ihr Potenzial zu erkennen und auszuleben. Dafür setze ich mich als selbstständiger Berater ein, nach 25 Jahren im Personalbereich, zumeist in Führungspositionen.</p>
    <h4>Meine Überzeugung</h4>
    <p>Weil es immer eine bessere Lösung gibt, strebe ich Win-Win-Win-Lösungen an. Und das unheimlich gerne. Für den Menschen und fürs Unternehmen. Menschlich und wirtschaftlich.</p>
    <h4>Meine Haltung</h4>
    <p>Vor ein paar Jahren während meiner Zeit als Leiter der Personalentwicklung sagte ein Personalvorstand mal ganz lakonisch im fränkischen Dialekt: „Am Ende geht's darum, sauba mit die Leut' umgehn." Dem habe ich nichts hinzuzufügen.</p>
    <span class="btn">Mehr über mich</span>
  </div>

  <div class="abs mark" style="top:3793px"></div>
  <h2 class="abs heading" style="top:3834px"><span class="rule"></span>Aktuelles aus dem Blog:<span class="rule"></span></h2>
  <div class="abs sub" style="top:3861px">Weil Wissen wirkt, wenn wir es teilen</div>
  <div class="abs blog" style="left:280px;top:3929px;width:281px;height:259px">
    <h3>Blogbeitrag 1</h3>
    <p>Weil es immer eine bessere Lösung gibt, strebe ich Win-Win-Win-Lösungen an. Und das unheimlich gerne. Für den Menschen und fürs...</p>
    <span class="btn">weiterlesen</span>
  </div>
  <div class="abs blog" style="left:640px;top:3929px;width:280px;height:259px">
    <h3>Blogbeitrag 2</h3>
    <p>Vor ein paar Jahren während meiner Zeit als Leiter der Personalentwicklung sagte ein Personalvorstand mal ganz lakonisch im fränkischen Dialekt...</p>
    <span class="btn">weiterlesen</span>
  </div>

  <footer class="abs footer"></footer>
  <div class="abs foot-dot"></div>
  <div class="abs foot-brand">
    <div class="name">Jonas Brenner</div>
    <div class="tag"><span class="rule"></span>Klar. Fair. Nachhaltig.<span class="rule"></span></div>
    <div class="claim">Lösungen für komplexe Personalsituationen</div>
  </div>
  <ul class="abs foot-nav" style="left:590px;top:4225px;width:220px">
    <li class="active"><span>Home</span></li>
    <li><span>Prozessberatung</span></li>
    <li><span>Situationsanalyse</span></li>
    <li><span>Energie-Coaching</span></li>
    <li><span>Speeches &amp; Vorträge</span></li>
  </ul>
  <ul class="abs foot-nav" style="left:860px;top:4231px;width:180px">
    <li>Über Mich</li>
    <li>Kontakt</li>
    <li>Datenschutz</li>
    <li>Impressum</li>
  </ul>
</main>
</body>
</html>
```